The Web Promotion Playbook for Yard & Patio Construction Crews

We need a book cover design that is for a book targeting landscape and outdoor living contractors that helps them grow their business using online marketing.

We run a business focused on this industry so you can see what we do: https://yardcrewgrowthworks.com/

The title is: The Web Promotion Playbook for Yard & Patio Construction Crews

The author is: Trent Varnholm
Some drafts have been done however they're still looking basic and somewhat amateur, we're looking for something that will stand out.

Target Market(s)

Landscape, Hardscape and Outdoor Living Contractors and Business Owners

Industry/Entity Type

Online Marketing

Font styles to use
Serif
Sans Serif

Requirements
Must have
• The part of the title that should stand out the most is the text "Web Promotion Playbook".
Should not have
• The color red

```html
<!DOCTYPE html>
<html lang="en">
<head>
<meta charset="utf-8">
<title>The Web Promotion Playbook for Yard &amp; Patio Construction Crews</title>
<link href="https://fonts.googleapis.com/css2?family=Oswald:wght@500;600;700&display=swap" rel="stylesheet">
<style>
  :root {
    --sky-deep: #1c4b80;
    --sky-mid: #3b78b0;
    --sky-glow: #cfe9f7;
    --map-teal: #3f8f96;
    --map-green: #5f9c8a;
    --night: #05080b;
    --night-edge: #101c22;
    --night-teal: #1d3a3c;
    --ink-light: #ffffff;
    --ink-soft: #eef6fc;
  }
  * { margin: 0; padding: 0; box-sizing: border-box; }
  html, body { width: 800px; height: 1200px; overflow: hidden; background: var(--sky-deep); }
  .cover {
    position: relative;
    width: 800px;
    height: 1200px;
    overflow: hidden;
    font-family: "Oswald", "Arial Narrow", sans-serif;
    color: var(--ink-light);
  }
  .map-artwork {
    position: absolute;
    inset: 0;
    background:
      linear-gradient(152deg, transparent 38%, rgba(225,242,252,0.55) 46%, rgba(255,255,255,0.7) 48%, rgba(225,242,252,0.5) 50%, transparent 58%),
      linear-gradient(28deg, transparent 44%, rgba(200,230,248,0.35) 50%, transparent 56%),
      radial-gradient(ellipse 300px 200px at 180px 470px, rgba(95,156,138,0.5), transparent 75%),
      radial-gradient(ellipse 260px 180px at 430px 820px, rgba(63,143,150,0.45), transparent 75%),
      radial-gradient(ellipse 520px 400px at 330px 560px, rgba(207,233,247,0.55), transparent 70%),
      linear-gradient(165deg, #4f8cc2 0%, var(--sky-mid) 35%, #2f6aa3 70%, var(--sky-deep) 100%);
  }
  .night-map { position: absolute; inset: 0; }
  .title-block {
    position: absolute;
    top: 60px;
    left: 0;
    width: 100%;
    text-align: center;
    text-shadow: 0 2px 6px rgba(10,30,60,0.45);
  }
  .title-lead {
    display: block;
    font-weight: 600;
    font-size: 66px;
    letter-spacing: 3px;
    line-height: 1.05;
  }
  .title-main {
    display: block;
    margin-top: 6px;
    font-weight: 700;
    font-size: 66px;
    letter-spacing: 50px;
    padding-left: 50px;
    line-height: 1.05;
  }
  .title-sub {
    display: block;
    margin-top: 14px;
    font-weight: 600;
    font-size: 28px;
    letter-spacing: 2.5px;
    color: var(--ink-soft);
  }
  .author {
    position: absolute;
    top: 1100px;
    left: 0;
    width: 800px;
    text-align: center;
    font-weight: 600;
    font-size: 28px;
    letter-spacing: 2px;
  }
</style>
</head>
<body>
  <div class="cover">
    <div class="map-artwork" role="img" aria-label="Glowing blue aerial city map with street grids, green park areas and bright diagonal light streaks"></div>
    <svg class="night-map" width="800" height="1200" viewBox="0 0 800 1200" role="img" aria-label="Stepped dark night-time map panels with faint teal streets rising from lower left to upper right">
      <defs>
        <linearGradient id="nightFill" x1="0" y1="0" x2="1" y2="1">
          <stop offset="0" stop-color="var(--night-teal)"/>
          <stop offset="0.45" stop-color="var(--night-edge)"/>
          <stop offset="1" stop-color="var(--night)"/>
        </linearGradient>
      </defs>
      <path d="M630 262 H800 V1200 H130 V1014 H342 V953 H503 V610 H630 Z" fill="url(#nightFill)" opacity="0.95"/>
    </svg>
    <header class="title-block">
      <h1>
        <span class="title-lead">THE WEB PROMOTION</span>
        <span class="title-main">PLAYBOOK</span>
        <span class="title-sub">FOR YARD &amp; PATIO CONSTRUCTION CREWS</span>
      </h1>
    </header>
    <p class="author">TRENT VARNHOLM</p>
  </div>
</body>
</html>
```